Microblading website contest - Make it colorful

Beauty salon focusing on microblading need a better website template. Please make a 1 page site mobile optimized and nicer layout with better color formulation. Would love interactive images in the site. You can use stock images and if approve we can pay for it.
Current site:
tessawynkelpeony.com

Inspiration:
https://framqueue.net/shots/41877260-Microblading-HomePage
https://framqueue.net/shots/7914026-Lunetto-Microblading-Eyebrow-Beauty-Salon-Pagewright-Theme

Target Market(s)

women

Industry/Entity Type

beauty salon

Number of Pages Required

1 page

Font styles to use
Serif
Decorative
Script

Requirements
Nice to have
• As pretty as possible

```html
<!DOCTYPE html>
<html lang="en">
<head>
<meta charset="utf-8">
<title>Microblading</title>
<link href="https://fonts.googleapis.com/css2?family=Playfair+Display:wght@400;700&family=PT+Serif:wght@400;700&family=Montserrat:wght@400;500&family=Inter:wght@600&display=swap" rel="stylesheet">
<style>
  :root {
    --bg-top: #2e2c29;
    --bg-bottom: #1c1c1a;
    --gold: #c9a45c;
    --gold-light: #e3c57f;
    --ink: #1f1c17;
    --white: #ffffff;
    --muted: #e6e2da;
    --frame: #4a4640;
  }
  * { margin: 0; padding: 0; box-sizing: border-box; }
  html, body { width: 1200px; height: 2302px; overflow: hidden; }
  body {
    position: relative;
    background: radial-gradient(ellipse at 55% 35%, var(--bg-top), var(--bg-bottom) 80%);
    color: var(--white);
    font-family: "PT Serif", serif;
  }
  .abs { position: absolute; }

  .status-time { left: 56px; top: 44px; font: 600 47px/1 "Inter", sans-serif; }
  .status-icons { right: 56px; top: 46px; }

  .site-name { left: 56px; top: 130px; font: 700 56px/1 "Playfair Display", serif; }
  .menu-icon { left: 1083px; top: 148px; }

  .brand-title { left: 56px; top: 258px; font: 700 55px/1 "Playfair Display", serif; color: var(--gold); }
  .brand-tagline { left: 56px; top: 330px; font: 400 27px/1 "PT Serif", serif; }

  .photo { overflow: hidden; }
  .thumb { top: 407px; height: 151px; border: 3px solid var(--frame); }

  .hero-photo { left: 795px; top: 209px; width: 377px; height: 375px;
    background:
      radial-gradient(ellipse 34% 40% at 50% 42%, #f0cdb0 0%, #e2ad8a 55%, rgba(226,173,138,0) 100%),
      radial-gradient(ellipse 60% 75% at 50% 50%, #b5582c 0%, #8e3f1f 55%, rgba(46,44,41,0) 100%);
  }

  .hero-rule { left: 0; top: 584px; width: 1200px; height: 3px; background: var(--gold); }

  .ceo-photo { left: 56px; top: 645px; width: 329px; height: 415px;
    background:
      radial-gradient(ellipse 38% 30% at 50% 36%, #eed6c6 0%, rgba(238,214,198,0) 100%),
      radial-gradient(ellipse 55% 60% at 50% 50%, #2a2220 0%, rgba(42,34,32,0) 100%),
      linear-gradient(180deg, #e8e6e3 0%, #d4d1cd 55%, #f2f1ef 100%);
  }
  .ceo-role { left: 427px; top: 655px; font: 400 40px/1 "Montserrat", sans-serif; letter-spacing: 1px; white-space: nowrap; }
  .ceo-name { left: 427px; top: 703px; font: 500 30px/1 "Montserrat", sans-serif; }
  .ceo-bio { left: 427px; top: 744px; font: 400 26.5px/42px "PT Serif", serif; color: var(--muted); white-space: nowrap; }
  .ceo-more { font-weight: 700; color: var(--white); }

  .section-title { left: 56px; font: 400 50px/1 "PT Serif", serif; color: var(--gold-light); }
  .section-rule { height: 8px; background: var(--gold-light); }

  .service-card { left: 56px; top: 1216px; width: 1088px; height: 241px; border-radius: 22px;
    background: var(--gold-light); overflow: hidden; color: var(--ink); }
  .service-photo { left: 0; top: 0; width: 271px; height: 241px;
    background:
      radial-gradient(ellipse 40% 35% at 70% 45%, #f1d9c8 0%, rgba(241,217,200,0) 100%),
      radial-gradient(ellipse 30% 30% at 25% 70%, #7fb6d6 0%, rgba(127,182,214,0) 100%),
      linear-gradient(135deg, #f2f0ed, #cfcac4 60%, #9d978f); }
  .service-name { left: 301px; top: 34px; font: 400 58px/1 "PT Serif", serif; }
  .service-desc { left: 301px; top: 118px; font: 400 40px/47px "PT Serif", serif; white-space: nowrap; }

  .dot { top: 1485px; width: 27px; height: 27px; border-radius: 50%; border: 3px solid var(--gold-light); }
  .dot.active { background: var(--gold-light); }

  .gallery { left: 56px; top: 1694px; width: 1088px; height: 418px;
    display: grid; grid-template-columns: repeat(5, 1fr); grid-template-rows: repeat(2, 1fr); }
  .gallery-item { border: 1px solid #2a2926; }
</style>
</head>
<body>
  <div class="abs status-time">9:41</div>
  <svg class="abs status-icons" width="210" height="40" viewBox="0 0 210 40" aria-hidden="true">
    <g fill="#fff">
      <rect x="0" y="24" width="9" height="12" rx="2"/><rect x="14" y="17" width="9" height="19" rx="2"/>
      <rect x="28" y="10" width="9" height="26" rx="2"/><rect x="42" y="3" width="9" height="33" rx="2"/>
      <path d="M98 36 l-7 -8 a11 11 0 0 1 14 0z"/>
      <path d="M80 19 a26 26 0 0 1 36 0 l-5 5 a19 19 0 0 0 -26 0z"/>
      <path d="M72 11 a38 38 0 0 1 52 0 l-5 5 a31 31 0 0 0 -42 0z"/>
      <rect x="142" y="6" width="60" height="30" rx="9" fill="none" stroke="#fff" stroke-width="3"/>
      <rect x="147" y="11" width="45" height="20" rx="5"/>
      <rect x="204" y="15" width="5" height="12" rx="2"/>
    </g>
  </svg>

  <header>
    <div class="abs site-name">Microblading</div>
    <svg class="abs menu-icon" width="54" height="40" viewBox="0 0 54 40" aria-label="Menu">
      <g fill="#fff"><rect y="2" width="54" height="6" rx="2"/><rect y="17" width="54" height="6" rx="2"/><rect y="32" width="54" height="6" rx="2"/></g>
    </svg>
  </header>

  <section class="intro">
    <h1 class="abs brand-title">Atelier Of Brows Tessa</h1>
    <p class="abs brand-tagline">&gt;&gt;&gt; Your personal eyebrow specialist</p>
    <div class="abs photo thumb" style="left:56px;width:142px;background:radial-gradient(ellipse 60% 40% at 50% 30%,#f3f1ee,rgba(243,241,238,0)),linear-gradient(180deg,#cfcbc5,#55514b 70%,#2f2c29);" role="img" aria-label="Training class in a bright studio"></div>
    <div class="abs photo thumb" style="left:212px;width:142px;background:radial-gradient(ellipse 50% 40% at 60% 55%,#e7c9b2,rgba(231,201,178,0)),linear-gradient(180deg,#8a7a6b,#4a4038);" role="img" aria-label="Students practising brow work"></div>
    <div class="abs photo thumb" style="left:363px;width:142px;background:radial-gradient(ellipse 45% 35% at 35% 25%,#e8cf6a,rgba(232,207,106,0)),radial-gradient(ellipse 40% 30% at 75% 30%,#f1dd8c,rgba(241,221,140,0)),linear-gradient(180deg,#3a3630,#25231f);" role="img" aria-label="Graduation celebration with gold balloons"></div>
    <div class="abs photo hero-photo" role="img" aria-label="Portrait of a woman with auburn hair"></div>
    <div class="abs hero-rule"></div>
  </section>

  <section class="ceo">
    <div class="abs photo ceo-photo" role="img" aria-label="Portrait of the salon founder"></div>
    <h2 class="abs ceo-role">THE LADY OF THE HOUR (CEO)</h2>
    <p class="abs ceo-name">Clara Wenholt</p>
    <p class="abs ceo-bio">Tessa has 7 years of microblading experience. She<br>graduated from VelaTouch United States. After, she studied<br>in Lumacademy, a global top brand from Germany. She was<br>personally guided by the brand CEO Marco Velin and the<br>first China Master Lin Haowen.<br><span class="ceo-more">Lihat Selengkapnya</span></p>
  </section>

  <section class="services">
    <h2 class="abs section-title" style="top:1093px;">Specialized Service</h2>
    <div class="abs section-rule" style="left:530px;top:1109px;width:614px;"></div>
    <article class="abs service-card">
      <div class="abs photo service-photo" role="img" aria-label="Client receiving a brow treatment"></div>
      <h3 class="abs service-name">Natural Brows</h3>
      <p class="abs service-desc">Microblading | Hand-drawing hair<br>lines</p>
    </article>
    <div class="abs dot active" style="left:530px;"></div>
    <div class="abs dot" style="left:586px;"></div>
    <div class="abs dot" style="left:642px;"></div>
  </section>

  <section class="gallery-section">
    <h2 class="abs section-title" style="top:1588px;">Our Gallery</h2>
    <div class="abs section-rule" style="left:363px;top:1600px;width:781px;"></div>
    <div class="abs gallery">
      <div class="gallery-item" style="background:radial-gradient(ellipse 45% 35% at 50% 75%,#f4f2ee,rgba(244,242,238,0)),linear-gradient(180deg,#d9d4cc,#7a736a);" role="img" aria-label="Graduate holding a certificate"></div>
      <div class="gallery-item" style="background:radial-gradient(ellipse 40% 45% at 55% 55%,#e2c4ad,rgba(226,196,173,0)),linear-gradient(180deg,#a8988a,#6f6359);" role="img" aria-label="Hand close-up"></div>
      <div class="gallery-item" style="background:radial-gradient(ellipse 45% 30% at 50% 78%,#d9c184,rgba(217,193,132,0)),linear-gradient(180deg,#3a3631,#221f1c);" role="img" aria-label="Class group photo"></div>
      <div class="gallery-item" style="background:radial-gradient(circle at 50% 22%,#faf7f0 0 12%,rgba(250,247,240,0) 30%),linear-gradient(180deg,#d8cbb9,#5e5045);" role="img" aria-label="Studio with ring light"></div>
      <div class="gallery-item" style="background:radial-gradient(ellipse 60% 30% at 50% 20%,#f0efec,rgba(240,239,236,0)),linear-gradient(180deg,#bdbab6,#4c4945);" role="img" aria-label="Training room"></div>
      <div class="gallery-item" style="background:radial-gradient(ellipse 35% 30% at 30% 25%,#9fc6e4,rgba(159,198,228,0)),linear-gradient(180deg,#d8dadb,#6f6a64);" role="img" aria-label="Presentation session"></div>
      <div class="gallery-item" style="background:radial-gradient(ellipse 40% 35% at 55% 45%,#d8b9a3,rgba(216,185,163,0)),linear-gradient(180deg,#c4c1bd,#2f2c2a);" role="img" aria-label="Brow procedure in progress"></div>
      <div class="gallery-item" style="background:radial-gradient(ellipse 30% 30% at 35% 40%,#fffdf4,rgba(255,253,244,0)),radial-gradient(ellipse 25% 25% at 70% 65%,#e8c772,rgba(232,199,114,0)),linear-gradient(180deg,#e9e5dd,#b6afa4);" role="img" aria-label="Flowers and tools"></div>
      <div class="gallery-item" style="background:radial-gradient(ellipse 60% 40% at 30% 15%,#d8b963,rgba(216,185,99,0)),linear-gradient(180deg,#6a5a3c,#2a2621);" role="img" aria-label="Artist at work"></div>
      <div class="gallery-item" style="background:radial-gradient(ellipse 50% 40% at 60% 30%,#f5f4f1,rgba(245,244,241,0)),linear-gradient(180deg,#d6d4d0,#65615c);" role="img" aria-label="Students practising"></div>
    </div>
  </section>
</body>
</html>
```